Traineeway.Asia, a social enterprise in Asia, needs a website!

I need a website designed for Traineeway.Asia, which is a social enterprise in Asia that connects potential interns with internship opportunities in the region.

Please read the attached wireframe and submit a homepage designs with text, based on the attached wireframe, from which we will choose and select the best design. Please note that we only want website designs; functionality, coding and programming are not required

The designer that provides the best designed home page, will then design all other pages of the website, and will receive the fee. We have already come up with one design (see wireframe in the attached doc) that designers may review for ideas.

University and graduate students in Asia.

Social

5+ page

Sans Serif

• I want a website that doesn't require a significant amount of scrolling, and is well-designed so that it is easy to understand the website's purpose, how to navigate around the website, and utilize it.
• Easy to see all elements of the website without scrolling.

```html
<!DOCTYPE html>
<html lang="en">
<head>
<meta charset="utf-8">
<title>Traineeway.Asia</title>
<link href="https://fonts.googleapis.com/css2?family=Open+Sans:wght@400;600;700&display=swap" rel="stylesheet">
<style>
:root{
  --sky:#4fcdfc;
  --white:#ffffff;
  --green:#6cbd34;
  --green-line:#86cc55;
  --blue:#1f5bab;
  --navy:#0f4f9c;
  --cyan:#09aef0;
  --ink:#1d1d1d;
  --text:#333333;
  --muted:#6b6b6b;
  --link:#25a6d8;
  --border:#cfcfcf;
  --band:#e4ebf3;
  --band-grey:#e6e6e6;
  --tint:#e5f6fd;
}
*{box-sizing:border-box;margin:0;padding:0}
html,body{width:1113px;height:1200px;overflow:hidden}
body{background:var(--sky);font-family:"Open Sans",Arial,sans-serif;color:var(--text);position:relative}
.page{position:absolute;left:137px;top:8px;width:835px;height:1149px;background:var(--white)}
.abs{position:absolute}
.brand{left:24px;top:36px;font-size:19px;font-weight:700;color:var(--navy);display:flex;align-items:center;gap:8px}
.brand-dot{width:12px;height:12px;border-radius:50%;background:var(--green)}
.header-social{right:36px;top:36px;font-size:13px;color:#b5b5b5;display:flex;gap:12px}
.nav{left:8px;top:87px;width:819px;height:40px;display:flex;background:var(--green)}
.nav a{color:var(--white);text-decoration:none;font-size:13px;display:flex;align-items:center;justify-content:center;border-right:1px solid var(--green-line)}
.nav a.active{background:var(--blue)}
.hero{left:10px;top:140px;width:554px;height:309px;border:1px solid var(--border);padding:2px}
.hero-photo{width:100%;height:100%;background:linear-gradient(135deg,#a7a29c,#7b746d 55%,#d8c98a)}
.hero-card{left:5px;top:64px;width:292px;min-height:135px;background:var(--white);padding:18px 16px 14px 22px}
.hero-card h1{font-size:18px;font-weight:400;color:var(--ink);margin-bottom:6px;white-space:nowrap}
.hero-card p{font-size:14.5px;line-height:19px;color:#444}
.panel{left:10px;width:554px;border:1px solid var(--border);padding:3px}
.panel-head{height:40px;display:flex;align-items:center;font-size:17px;font-weight:600;color:var(--ink);padding-left:8px}
.jobs{top:463px;height:310px}
.jobs .panel-head{background:var(--band)}
.job-grid{display:grid;grid-template-columns:1fr 1fr;column-gap:12px;padding:8px 14px 0 14px}
.job{font-size:12px;line-height:19px;color:#333;padding:6px 4px;border-bottom:1px solid #dcdcdc}
.job:nth-last-child(-n+2){border-bottom:none}
.job.short{height:66px}
.job.tall{height:80px}
.btn{display:inline-block;background:var(--navy);color:var(--white);font-size:10.5px;font-weight:600;padding:2px 11px}
.jobs .btn{position:absolute;right:24px;bottom:10px}
.resources{top:785px;height:350px}
.resources .panel-head{background:var(--band-grey);padding-left:17px}
.res-thumb{left:20px;top:83px;width:132px;height:102px;background:linear-gradient(135deg,#e8eef3,#5e6c7b 60%,#1d2530)}
.res-body{left:171px;top:80px;width:367px}
.res-body h2{font-size:17px;font-weight:600;color:var(--ink);margin-bottom:10px}
.res-body p{font-size:12.5px;line-height:20px;color:#333;margin-bottom:8px}
.resources .btn{position:absolute;right:24px;bottom:12px}
.follow{left:579px;top:141px;width:248px;height:78px;background:var(--cyan);color:var(--white);display:flex;align-items:center}
.follow-label{font-size:17px;padding-left:18px;width:132px}
.follow-sep{width:1px;height:58px;background:var(--white);margin-right:14px}
.follow-names{font-size:13px;font-weight:600;line-height:20px}
.feed{left:579px;top:235px;width:248px;height:898px;border:1px solid var(--border);padding:9px 7px}
.item{height:140px;border:1px solid var(--border);margin-bottom:8px;position:relative;padding:8px 4px}
.item-badge{position:absolute;left:8px;top:12px;width:52px;height:72px;background:#1b1b1b}
.item-badge.b2{background:#3a3f55}
.item-badge.b3{background:linear-gradient(#5f8dc0,#8a6e56)}
.item-badge.b4{background:#f0f4f9}
.item-badge.b4::after{content:"";position:absolute;left:10px;top:16px;width:32px;height:32px;border-radius:50%;background:#2a6db5}
.item-text{position:absolute;left:64px;top:18px;width:170px}
.item-title{font-size:12.5px;color:var(--ink);margin-bottom:4px}
.item-desc{font-size:12px;line-height:15px;color:var(--muted);padding-left:2px}
.item-desc span{color:var(--link)}
.item-cta{position:absolute;left:8px;right:4px;bottom:8px;height:34px;background:var(--tint);display:flex;align-items:center;justify-content:center;gap:10px;font-size:13px;color:var(--ink)}
.footer{position:absolute;left:0;top:1173px;width:1113px;text-align:center;font-size:11px;color:#3c6e86}
</style>
</head>
<body>
<div class="page">
  <div class="abs brand"><span class="brand-dot"></span>Traineeway.Asia</div>
  <div class="abs header-social"><span>Friendsly</span><span>Chirper</span></div>

  <nav class="abs nav">
    <a class="active" style="width:104px">Home</a>
    <a style="width:133px">About Us</a>
    <a style="width:164px">Search Internships</a>
    <a style="width:125px">Login</a>
    <a style="width:135px">Registration</a>
    <a style="width:158px;border-right:none">For Employers</a>
  </nav>

  <section class="abs hero">
    <div class="hero-photo" role="img" aria-label="Photo of a smiling student in a costume hat at a meeting table"></div>
    <div class="abs hero-card">
      <h1>Ready To Get Your Feet Wet?</h1>
      <p>Traineeway. Asia is apowerful network that helps talented students breaking through the professional world.</p>
    </div>
  </section>

  <section class="abs panel jobs">
    <div class="panel-head">FEATURED JOBS</div>
    <div class="job-grid">
      <div class="job tall">Lorem Ipsum is simply dummy text of the printing and typesetting industry. Lorem Ipsum has been the industry's.</div>
      <div class="job tall">Lorem Ipsum is simply dummy text of the printing and typesetting industry. Lorem Ipsum has been the industry's.</div>
      <div class="job short">Lorem Ipsum is simply dummy text of the printing and typesetting industry.</div>
      <div class="job short">Lorem Ipsum is simply dummy text of the printing and typesetting industry.</div>
      <div class="job tall">Lorem Ipsum is simply dummy text of the printing and typesetting industry. Lorem Ipsum has been the industry's.</div>
      <div class="job tall">Lorem Ipsum is simply dummy text of the printing and typesetting industry. Lorem Ipsum has been the industry's.</div>
    </div>
    <span class="btn">read more..</span>
  </section>

  <section class="abs panel resources">
    <div class="panel-head">RESOURCES</div>
    <div class="abs res-thumb" role="img" aria-label="Photo of a hand typing on a keyboard"></div>
    <div class="abs res-body">
      <h2>Resume / Cover Letter Tips</h2>
      <p>Lorem Ipsum is simply dummy text of the printing and typeset-ting industry. Lorem Ipsum has been the industry's.  Standard dummy text ever since the when an unknown printer took a galley of type and scrambled it to make a type specimen book. It has survived not only five centuries,</p>
      <p>Lorem Ipsum is simply dummy text of the printing and typeset-ting industry. Lorem Ipsum has been the industry's.  Standard dummy text ever since the when an unknown printer took a galley of type and scrambled.</p>
    </div>
    <span class="btn">read more..</span>
  </section>

  <aside class="abs follow">
    <div class="follow-label">Follow Us On</div>
    <div class="follow-sep"></div>
    <div class="follow-names">Friendsly<br>Chirper</div>
  </aside>

  <aside class="abs feed">
    <div class="item"><div class="item-badge"></div><div class="item-text"><div class="item-title">Quillpost @ Quillpost - 23m</div><div class="item-desc">Lorem Ipsum is simply dummy text of the <span>typesetting industry.</span></div></div><div class="item-cta"><svg width="12" height="15" viewBox="0 0 12 15"><path d="M1 1h6l4 4v9H1z M7 1v4h4" fill="none" stroke="#333" stroke-width="1.2"/></svg>View Summary</div></div>
    <div class="item"><div class="item-badge b2"></div><div class="item-text"><div class="item-title">Quillpost @ Quillpost - 23m</div><div class="item-desc">Lorem Ipsum is simply dummy text of the <span>typesetting industry.</span></div></div><div class="item-cta"><svg width="12" height="15" viewBox="0 0 12 15"><path d="M1 1h6l4 4v9H1z M7 1v4h4" fill="none" stroke="#333" stroke-width="1.2"/></svg>View Summary</div></div>
    <div class="item"><div class="item-badge b3" role="img" aria-label="Photo of a campus building"></div><div class="item-text"><div class="item-title">Quillpost @ Quillpost - 23m</div><div class="item-desc">Lorem Ipsum is simply dummy text of the <span>typesetting industry.</span></div></div><div class="item-cta"><svg width="12" height="15" viewBox="0 0 12 15"><path d="M1 1h6l4 4v9H1z M7 1v4h4" fill="none" stroke="#333" stroke-width="1.2"/></svg>View Summary</div></div>
    <div class="item"><div class="item-badge b4"></div><div class="item-text"><div class="item-title">Quillpost @ Quillpost - 23m</div><div class="item-desc">Lorem Ipsum is simply dummy text of the <span>typesetting industry.</span></div></div><div class="item-cta"><svg width="12" height="15" viewBox="0 0 12 15"><path d="M1 1h6l4 4v9H1z M7 1v4h4" fill="none" stroke="#333" stroke-width="1.2"/></svg>View Summary</div></div>
    <div class="item"><div class="item-badge b3" role="img" aria-label="Photo of a campus building"></div><div class="item-text"><div class="item-title">Quillpost @ Quillpost - 23m</div><div class="item-desc">Lorem Ipsum is simply dummy text of the <span>typesetting industry.</span></div></div><div class="item-cta"><svg width="12" height="15" viewBox="0 0 12 15"><path d="M1 1h6l4 4v9H1z M7 1v4h4" fill="none" stroke="#333" stroke-width="1.2"/></svg>View Summary</div></div>
    <div class="item"><div class="item-badge b4"></div><div class="item-text"><div class="item-title">Quillpost @ Quillpost - 23m</div><div class="item-desc">Lorem Ipsum is simply dummy text of the <span>typesetting industry.</span></div></div><div class="item-cta"><svg width="12" height="15" viewBox="0 0 12 15"><path d="M1 1h6l4 4v9H1z M7 1v4h4" fill="none" stroke="#333" stroke-width="1.2"/></svg>View Summary</div></div>
  </aside>
</div>
<div class="footer">© 2015 All rights resesrved.</div>
</body>
</html>
```